IT Company needs full suite of stationery

Our company 4627 Vantrel Works Ltd. is an IT company based in Toronto, Canada. Based on our logo we would like to see business cards(front and back), letterhead, envelope, brochure template. Design would be simple, not too bright, modern but can be used for many years, good theme throughout. Our official logo is the the fullcolor_a, full company name is 4627 Vantrel Works Ltd., Please include full company name on all pieces. Logo can be modified to be the graphic only with the "4627 Works", I have cropped it myself for a couple files but I am no designer. We will provide lots of feedback so post early and often.
Updates

Project Deadline Extended
Reason: Very busy around the holidays, like a lot of the designs currently submitted, will definitely be picking one. Thanks for your submissions and merry Christmas and Happy New Year to everyone.

Industry/Entity Type

Business

```html
<!DOCTYPE html>
<html lang="en">
<head>
<meta charset="utf-8">
<title>4627 Works — Stationery Suite</title>
<link rel="stylesheet" href="https://fonts.googleapis.com/css2?family=Open+Sans:wght@400;600;700&family=EB+Garamond:wght@400&display=swap">
<style>
  :root {
    --charcoal: #2f2c2b;
    --charcoal-deep: #1f1d1c;
    --stage: #2a2a2a;
    --green: #3aa04c;
    --green-light: #5cb86c;
    --white: #ffffff;
    --paper: #f4f4f4;
    --ink: #4a4a4a;
    --muted: #8a8a8a;
  }
  * { box-sizing: border-box; margin: 0; padding: 0; }
  html, body { width: 1200px; height: 1000px; overflow: hidden; }
  body {
    background: var(--stage);
    font-family: "Open Sans", Arial, sans-serif;
    color: var(--ink);
    position: relative;
  }
  .piece { position: absolute; overflow: hidden; }

  /* Brand name set as plain text */
  .brand-name {
    font-family: "Open Sans", Arial, sans-serif;
    font-weight: 700;
    color: var(--charcoal);
    letter-spacing: 0.02em;
    white-space: nowrap;
  }
  .brand-name.on-dark { color: var(--white); }

  /* Side strip */
  .side-strip { left: 0; top: 0; width: 216px; height: 1000px; }
  .side-strip__top { height: 450px; background: var(--charcoal); display: flex; align-items: center; justify-content: center; padding-bottom: 150px; }
  .side-strip__top .brand-name { font-size: 22px; }
  .side-strip__band { height: 70px; background: var(--white); }
  .side-strip__bottom { height: 480px; background: var(--green); }

  /* Letterhead */
  .letterhead { left: 250px; top: 30px; width: 310px; height: 440px; background: var(--white); }
  .letterhead__header { height: 86px; background: var(--charcoal); position: relative; }
  .logo-box { position: absolute; background: var(--white); display: flex; align-items: center; justify-content: center; }
  .letterhead .logo-box { right: 14px; top: 0; width: 96px; height: 34px; }
  .letterhead .logo-box .brand-name { font-size: 12px; }
  .contact-block { position: absolute; left: 14px; bottom: 10px; display: flex; gap: 7px; align-items: flex-start; }
  .contact-block__dot { width: 18px; height: 18px; border-radius: 50%; background: var(--white); flex: none; margin-top: 2px; }
  .contact-block p { font-size: 5px; line-height: 1.45; color: #cfcfcf; }
  .contact-block .contact-name { color: var(--green-light); font-weight: 700; }
  .letter-body { padding: 26px 30px 0; font-family: "EB Garamond", Georgia, serif; font-size: 6.5px; line-height: 1.6; color: var(--ink); }
  .letter-body p { margin-bottom: 8px; }
  .letterhead__footer { position: absolute; left: 0; bottom: 0; width: 100%; height: 14px; background: var(--green); }

  /* Envelope */
  .envelope { left: 590px; top: 30px; width: 580px; height: 280px; background: var(--white); }
  .envelope__header { height: 86px; background: var(--charcoal); position: relative; }
  .envelope .logo-box { right: 20px; top: 0; width: 110px; height: 36px; }
  .envelope .logo-box .brand-name { font-size: 13px; }
  .envelope__window { position: absolute; right: 30px; top: 66px; width: 90px; height: 30px; border: 1px solid #e6e6e6; background: var(--white); }
  .envelope__mark { position: absolute; left: 50%; top: 108px; transform: translateX(-50%); display: flex; align-items: center; gap: 6px; }
  .envelope__mark .dot { width: 12px; height: 12px; border-radius: 50%; background: var(--green); }
  .envelope__mark .brand-name { font-size: 11px; }
  .envelope__flap { position: absolute; left: 0; bottom: 0; width: 580px; height: 130px; }

  /* Business cards */
  .card { width: 200px; height: 340px; top: 560px; box-shadow: 0 0 0 6px #d8d8d8; }
  .card-front { left: 260px; background: linear-gradient(#4a4644, #2e2b2a); }
  .card-front__mark { position: absolute; left: 50%; top: 40px; transform: translateX(-50%); display: flex; align-items: center; gap: 6px; }
  .card-front__mark .dot { width: 12px; height: 12px; border-radius: 50%; background: var(--white); }
  .card-front__mark .brand-name { font-size: 11px; }
  .card-photo { position: absolute; left: 0; top: 100px; width: 100%; height: 150px; background: linear-gradient(180deg, #1c1c1c 0%, #6f6f6f 55%, #2a2a2a 100%); }
  .card-front .name-box { position: absolute; left: 40px; top: 140px; width: 120px; height: 44px; background: var(--paper); display: flex; align-items: center; justify-content: center; }
  .card-front .name-box .brand-name { font-size: 15px; }
  .green-tab { position: absolute; background: var(--green); color: var(--white); font-size: 8px; letter-spacing: 0.08em; display: flex; align-items: center; justify-content: center; text-transform: uppercase; }
  .card-front .green-tab { left: 60px; top: 184px; width: 100px; height: 18px; }

  .card-back { left: 490px; background: linear-gradient(#fbfbfb, #e9e9e9); padding: 26px 22px; }
  .card-back__mark { display: flex; align-items: center; gap: 6px; margin-bottom: 26px; }
  .card-back__mark .dot { width: 14px; height: 14px; border-radius: 50%; background: var(--green); }
  .card-back__mark .brand-name { font-size: 10px; }
  .card-back .name-bar { width: 130px; height: 34px; background: #222; display: flex; align-items: center; justify-content: center; margin-bottom: 22px; }
  .card-back .name-bar .brand-name { font-size: 14px; }
  .card-back .person { color: var(--green); font-size: 13px; letter-spacing: 0.06em; }
  .card-back .role { font-size: 9px; color: #444; margin-bottom: 12px; }
  .card-back .details { font-size: 7px; line-height: 1.6; color: var(--ink); }

  /* Brochure */
  .brochure { left: 730px; top: 340px; width: 440px; height: 620px; background: linear-gradient(#4d4947, #2f2c2b 70%, #3a3735); box-shadow: 0 0 0 8px #e2e2e2; }
  .brochure__mark { position: absolute; right: 60px; top: 70px; display: flex; align-items: center; gap: 8px; }
  .brochure__mark .dot { width: 16px; height: 16px; border-radius: 50%; background: var(--white); }
  .brochure__mark .brand-name { font-size: 15px; }
  .brochure .card-photo { top: 150px; height: 240px; }
  .brochure .name-box { position: absolute; right: 40px; top: 200px; width: 200px; height: 70px; background: var(--paper); display: flex; align-items: center; justify-content: center; }
  .brochure .name-box .brand-name { font-size: 24px; }
  .brochure .green-tab { right: 40px; top: 270px; width: 200px; height: 26px; font-size: 11px; }
</style>
</head>
<body>

  <aside class="piece side-strip">
    <div class="side-strip__top"><span class="brand-name on-dark">4627 Works</span></div>
    <div class="side-strip__band"></div>
    <div class="side-strip__bottom"></div>
  </aside>

  <section class="piece letterhead">
    <header class="letterhead__header">
      <div class="logo-box"><span class="brand-name">4627 Works</span></div>
      <div class="contact-block">
        <span class="contact-block__dot"></span>
        <div>
          <p class="contact-name">LOREM IPSUM</p>
          <p>Lorem ipsum dolor sit amet, consectetur adipiscing elit.</p>
          <p>+ 00 0000 0000 00</p>
          <p>companyname@domain.com</p>
          <p>www.companyname.com</p>
        </div>
      </div>
    </header>
    <div class="letter-body">
      <p>Mr. Lorem Ipsum</p>
      <p>Donec rutrum congue leo eget malesuada. Donec sollicitudin molestie malesuada. Cras ultricies ligula sed magna dictum porta, accumsan id imperdiet et, porttitor at sem. Vivamus suscipit tortor eget felis porttitor volutpat. Curae.</p>
      <p>Donec velit neque, auctor sit amet aliquam vel, ullamcorper sit amet ligula. Praesent sapien massa, convallis a pellentesque nec, egestas non nisi.</p>
      <p>Vestibulum ac diam sit amet quam vehicula elementum sed sit amet dui. Pellentesque in ipsum id orci porta dapibus. Nulla porttitor accumsan tincidunt.</p>
      <p>Vestibulum ante ipsum primis in faucibus orci luctus et ultrices posuere cubilia curae.</p>
    </div>
    <div class="letterhead__footer"></div>
  </section>

  <section class="piece envelope">
    <header class="envelope__header">
      <div class="logo-box"><span class="brand-name">4627 Works</span></div>
      <div class="contact-block">
        <span class="contact-block__dot"></span>
        <div>
          <p class="contact-name">LOREM IPSUM</p>
          <p>Lorem ipsum dolor sit amet, consectetur adipiscing elit.</p>
          <p>+ 00 0000 0000 00</p>
          <p>companyname@domain.com</p>
          <p>www.companyname.com</p>
        </div>
      </div>
    </header>
    <div class="envelope__mark"><span class="dot"></span><span class="brand-name">4627 Works</span></div>
    <svg class="envelope__flap" viewBox="0 0 580 130" aria-hidden="true">
      <path d="M0 60 Q0 20 40 20 L540 20 Q580 20 580 0 L580 130 L0 130 Z" fill="#3aa04c"/>
    </svg>
  </section>

  <section class="piece card card-front">
    <div class="card-front__mark"><span class="dot"></span><span class="brand-name on-dark">4627 Works</span></div>
    <div class="card-photo" role="img" aria-label="Photograph of a server room corridor in dark grey tones"></div>
    <div class="name-box"><span class="brand-name">4627 Works</span></div>
    <div class="green-tab">Lorem Ipsum</div>
  </section>

  <section class="piece card card-back">
    <div class="card-back__mark"><span class="dot"></span><span class="brand-name">4627 Works</span></div>
    <div class="name-bar"><span class="brand-name on-dark">4627 Works</span></div>
    <p class="person">LOREM IPSUM</p>
    <p class="role">Title</p>
    <p class="details">+ 00 0000 0000 00<br>companyname@domain.com<br>www.companyname.com</p>
  </section>

  <section class="piece brochure">
    <div class="brochure__mark"><span class="dot"></span><span class="brand-name on-dark">4627 Works</span></div>
    <div class="card-photo" role="img" aria-label="Photograph of a server room corridor in dark grey tones"></div>
    <div class="name-box"><span class="brand-name">4627 Works</span></div>
    <div class="green-tab">Lorem Ipsum</div>
  </section>

</body>
</html>
```